M Zyvantics Buisness Cards

I need a technology focused clean business card for my employees. I have attached out logo to include in the mocks. We're a modern tech consulting firm that drives to interface humanity with technology in a truly cohesive fashion.

```html
<!DOCTYPE html>
<html lang="en">
<head>
<meta charset="utf-8">
<title>M Zyvantics Business Cards</title>
<link rel="stylesheet" href="https://fonts.googleapis.com/css2?family=Arimo:wght@400;700&display=swap">
<style>
:root{
  --bg:#d3dcdd;
  --paper:#ffffff;
  --ink:#1e1e1e;
  --black:#000000;
  --blue:#1f74bd;
  --grey:#808285;
  --rule:#8a8a8a;
}
*{margin:0;padding:0;box-sizing:border-box}
html,body{width:1200px;height:1200px;overflow:hidden}
body{background:var(--bg);font-family:"Arimo",Arial,sans-serif;color:var(--ink);position:relative}
.card{position:absolute;left:271px;width:661px;height:380px;background:var(--paper);overflow:hidden}
.card--front{top:154px}
.card--back{top:666px;height:382px}
.band{position:absolute;top:0;bottom:0}
.card--front .band-left{left:0;width:30px;background:var(--black)}
.card--front .band-accent{left:30px;width:3px;background:var(--blue)}
.card--front .band-right{right:0;width:11px;background:var(--blue)}
.card--back .band-left{left:0;width:44px;background:var(--black)}
.card--back .band-right{right:0;width:17px;background:var(--blue)}
.brand{position:absolute;display:flex;align-items:center;color:var(--grey);font-weight:700;white-space:nowrap}
.brand-dot{border-radius:50%;background:var(--blue);flex:none}
.card--front .brand{left:0;right:0;top:160px;justify-content:center;font-size:52px;gap:16px}
.card--front .brand-dot{width:26px;height:26px}
.card--back .brand{right:36px;top:292px;font-size:32px;gap:10px}
.card--back .brand-dot{width:16px;height:16px}
.icon{position:absolute;left:25px;width:38px;height:38px}
.person{position:absolute;left:75px;top:38px}
.person-name{font-size:28px;font-weight:700;letter-spacing:.2px}
.person-name .last{color:var(--blue)}
.person-role{font-size:17px;margin-top:2px}
.rule{position:absolute;left:75px;width:196px;height:1.5px;background:var(--rule)}
.rule--accent{top:118px;background:var(--blue)}
.detail{position:absolute;left:75px;font-size:18px;line-height:21px}
</style>
</head>
<body>
<section class="card card--front" aria-label="Card front">
  <div class="band band-left"></div>
  <div class="band band-accent"></div>
  <div class="band band-right"></div>
  <div class="brand"><span class="brand-dot"></span>M Zyvantics</div>
</section>

<section class="card card--back" aria-label="Card back">
  <div class="band band-left"></div>
  <div class="band band-right"></div>

  <svg class="icon" style="top:37px" viewBox="0 0 38 38" aria-hidden="true">
    <circle cx="19" cy="19" r="18" fill="#fff"/><circle cx="19" cy="19" r="15.5" fill="var(--blue)"/>
    <circle cx="19" cy="15" r="5" fill="#fff"/><path d="M10 27c1-5 5-7 9-7s8 2 9 7z" fill="#fff"/>
  </svg>
  <div class="person">
    <div class="person-name">MARA <span class="last">QUILL</span></div>
    <div class="person-role">MANAGER</div>
  </div>
  <div class="rule rule--accent"></div>

  <svg class="icon" style="top:167px" viewBox="0 0 38 38" aria-hidden="true">
    <circle cx="19" cy="19" r="18" fill="#fff"/><circle cx="19" cy="19" r="15.5" fill="var(--blue)"/>
    <path d="M13 10l3 0 2 5-2 2c1 2 3 4 5 5l2-2 5 2 0 3c0 1-1 2-2 2-8 0-15-7-15-15 0-1 1-2 2-2z" fill="#fff"/>
  </svg>
  <div class="detail" style="top:164px">012-555-0147<br>012-555-0147</div>
  <div class="rule" style="top:218px"></div>

  <svg class="icon" style="top:237px" viewBox="0 0 38 38" aria-hidden="true">
    <circle cx="19" cy="19" r="18" fill="#fff"/><circle cx="19" cy="19" r="15.5" fill="var(--blue)"/>
    <rect x="10" y="13" width="18" height="12" fill="#fff"/><path d="M10 13l9 7 9-7M10 25l7-6M28 25l-7-6" stroke="var(--blue)" stroke-width="1.4" fill="none"/>
  </svg>
  <div class="detail" style="top:234px">info@zyvantics.com<br>www.zyvantics.com</div>
  <div class="rule" style="top:288px"></div>

  <svg class="icon" style="top:306px" viewBox="0 0 38 38" aria-hidden="true">
    <circle cx="19" cy="19" r="18" fill="#fff"/><circle cx="19" cy="19" r="15.5" fill="var(--blue)"/>
    <path d="M19 30c-5-6-7-9-7-12a7 7 0 0114 0c0 3-2 6-7 12z" fill="#fff"/><circle cx="19" cy="18" r="2.8" fill="var(--blue)"/>
  </svg>
  <div class="detail" style="top:304px">418 Linden Crest Road<br>Halvern, AK 99812</div>

  <div class="brand"><span class="brand-dot"></span>M Zyvantics</div>
</section>
</body>
</html>
```